Providing Back Office Solutions to Financial Advisors and Attorney Needs a Business Card Design

Need a Business Card Design that speaks to Financial Advisor and Attorneys. Some of the word that come to mind is Clean/Simple & Futuristic.

Industry/Entity Type

Business

```html
<!DOCTYPE html>
<html lang="en">
<head>
<meta charset="utf-8">
<title>Veritan Back Office Solutions – Business Card</title>
<link href="https://fonts.googleapis.com/css2?family=Lato:wght@400;700&display=swap" rel="stylesheet">
<style>
  :root {
    --bg-dark: #2b2b2b;
    --bg-mid: #474747;
    --brand-blue: #1466a8;
    --brand-blue-light: #0a84c8;
    --brand-blue-deep: #17538f;
    --card-white: #ffffff;
    --ink: #2a2a2a;
    --on-blue: #ffffff;
  }
  * { margin: 0; padding: 0; box-sizing: border-box; }
  html, body { width: 1200px; height: 900px; overflow: hidden; }
  body {
    background: radial-gradient(ellipse at 50% 40%, var(--bg-mid), var(--bg-dark) 75%);
    font-family: "Lato", Arial, sans-serif;
    display: flex;
    align-items: center;
    justify-content: center;
    gap: 40px;
  }
  .card {
    width: 510px;
    height: 292px;
    border-radius: 4px;
    position: relative;
    box-shadow: 0 18px 40px rgba(0,0,0,.45);
  }

  /* White contact side */
  .card--contact {
    background: var(--card-white);
    display: flex;
    align-items: center;
    padding: 0 34px;
  }
  .brand-mark {
    display: flex;
    align-items: center;
    gap: 10px;
    width: 190px;
  }
  .brand-mark__square {
    width: 26px; height: 26px;
    background: var(--brand-blue);
  }
  .brand-mark__name {
    font-size: 30px;
    font-weight: 700;
    color: var(--brand-blue);
    letter-spacing: 1px;
  }
  .divider {
    width: 1.5px;
    height: 150px;
    background: var(--brand-blue-light);
    margin: 0 26px 0 6px;
  }
  .contact {
    color: var(--ink);
    font-size: 14.5px;
    line-height: 1.3;
  }
  .contact__name {
    font-size: 21px;
    font-weight: 700;
    color: var(--brand-blue);
  }
  .contact__title { margin-bottom: 6px; }
  .contact__address { margin-bottom: 6px; }
  .contact__row { display: flex; align-items: center; gap: 8px; }
  .contact__row svg { width: 12px; height: 12px; fill: var(--brand-blue); flex: none; }

  /* Blue brand side */
  .card--brand {
    background: radial-gradient(ellipse at 58% 42%, var(--brand-blue-light), var(--brand-blue) 55%, var(--brand-blue-deep));
    color: var(--on-blue);
  }
  .brand-lockup {
    position: absolute;
    left: 78px; top: 86px;
    display: flex;
    align-items: center;
  }
  .brand-lockup__square {
    width: 50px; height: 50px;
    background: var(--on-blue);
    margin-right: 22px;
  }
  .brand-lockup__rule {
    width: 1.5px; height: 96px;
    background: rgba(255,255,255,.85);
    margin-right: 20px;
  }
  .brand-lockup__name {
    font-size: 54px;
    font-weight: 700;
    letter-spacing: 3px;
    line-height: 1;
  }
  .brand-lockup__tagline {
    font-size: 15px;
    letter-spacing: 1.6px;
    margin-top: 8px;
  }
  .brand-url {
    position: absolute;
    left: 78px; bottom: 40px;
    font-size: 14px;
    letter-spacing: .5px;
  }
</style>
</head>
<body>
  <section class="card card--contact">
    <div class="brand-mark">
      <span class="brand-mark__square"></span>
      <span class="brand-mark__name">VERITAN</span>
    </div>
    <div class="divider"></div>
    <div class="contact">
      <div class="contact__name">Daniel Archer</div>
      <div class="contact__title">Manager</div>
      <div class="contact__address">418 Cedar Row<br>Austin, TX 78701</div>
      <div class="contact__row">
        <svg viewBox="0 0 24 24"><path d="M6.6 10.8a15.1 15.1 0 0 0 6.6 6.6l2.2-2.2c.3-.3.7-.4 1-.2 1.1.4 2.3.6 3.6.6.6 0 1 .4 1 1V20c0 .6-.4 1-1 1A17 17 0 0 1 3 4c0-.6.4-1 1-1h3.5c.6 0 1 .4 1 1 0 1.3.2 2.5.6 3.6.1.3 0 .7-.2 1z"/></svg>
        <span>555 010 2400</span>
      </div>
      <div class="contact__row">
        <svg viewBox="0 0 24 24"><path d="M6 3h10l2 2v4h2a2 2 0 0 1 2 2v8h-4v2H6v-2H2v-8a2 2 0 0 1 2-2h2zm2 2v4h8V6l-1-1zm0 10v4h8v-4z"/></svg>
        <span>555 010 2401</span>
      </div>
      <div class="contact__row">
        <svg viewBox="0 0 24 24"><path d="M2 5h20v14H2zm2 2v.5l8 5.5 8-5.5V7zm0 3v7h16v-7l-8 5.5z"/></svg>
        <span>info@veritanbo.com</span>
      </div>
      <div class="contact__row">
        <svg viewBox="0 0 24 24"><path d="M12 2a10 10 0 1 0 0 20 10 10 0 0 0 0-20zm6.9 9h-3a15 15 0 0 0-1.3-5.6A8 8 0 0 1 18.9 11zM12 4.1c1 1.3 1.8 3.9 1.9 6.9h-3.8c.1-3 .9-5.6 1.9-6.9zM9.4 5.4A15 15 0 0 0 8.1 11h-3a8 8 0 0 1 4.3-5.6zM5.1 13h3a15 15 0 0 0 1.3 5.6A8 8 0 0 1 5.1 13zm6.9 6.9c-1-1.3-1.8-3.9-1.9-6.9h3.8c-.1 3-.9 5.6-1.9 6.9zm2.6-1.3a15 15 0 0 0 1.3-5.6h3a8 8 0 0 1-4.3 5.6z"/></svg>
        <span>www.veritanbo.com</span>
      </div>
    </div>
  </section>

  <section class="card card--brand">
    <div class="brand-lockup">
      <span class="brand-lockup__square"></span>
      <span class="brand-lockup__rule"></span>
      <div>
        <div class="brand-lockup__name">VERITAN</div>
        <div class="brand-lockup__tagline">BACK OFFICE SOLUTIONS</div>
      </div>
    </div>
    <div class="brand-url">www.veritanbo.com</div>
  </section>
</body>
</html>
```